World domination merchandise

We need an illustration to print on a notebook (maybe eventually on other kinds of merchandise). We would like the words "Mes plans de domination mondiale" (which means "my world domination plans") in a calligraphy-like font, with maybe a world map, a globe, a flag... It has to be consistent with the vibe of our company, which is named "La Clairière" (The clearing). We are managing a community of entrepreneurs on a web-platform that is regrouping a forum and an online courses portal. Here are some keywords that represent our brand: vintage (in a modern way, if that makes sense), World War II, 40's/50's, entrepreneurship, web-marketing, community, sodality, collaboration.

I've attached a few image we like for inspiration

```html
<!DOCTYPE html>
<html lang="fr">
<head>
<meta charset="utf-8">
<title>Mes plans de domination mondiale</title>
<link rel="stylesheet" href="https://fonts.googleapis.com/css2?family=Frank+Ruhl+Libre:wght@700;900&display=swap">
<style>
  :root {
    --ink: #000000;
    --paper: #ffffff;
    --globe-tone: #cfcfcf;
  }
  html, body {
    margin: 0;
    padding: 0;
    width: 1200px;
    height: 1000px;
    overflow: hidden;
    background: var(--paper);
  }
  .notebook-emblem {
    display: block;
    width: 1200px;
    height: 1000px;
  }
  .headline {
    font-family: "Frank Ruhl Libre", Georgia, serif;
    font-weight: 900;
    fill: var(--ink);
    text-anchor: middle;
  }
  .ribbon-word {
    font-family: "Frank Ruhl Libre", Georgia, serif;
    font-weight: 700;
    fill: var(--ink);
    text-anchor: middle;
  }
  .rule-bar { fill: var(--ink); }
  .globe-area { fill: var(--globe-tone); stroke: var(--ink); stroke-width: 5; }
  .ribbon-part { fill: var(--paper); stroke: var(--ink); stroke-width: 4; stroke-linejoin: round; }
  .pointer { fill: var(--paper); stroke: var(--ink); stroke-width: 3.5; stroke-linejoin: round; }
</style>
</head>
<body>
<svg class="notebook-emblem" viewBox="480 131 850 708" xmlns="http://www.w3.org/2000/svg">
  <defs>
    <polygon id="pointer-arrow" class="pointer" points="-42,-6 -13,-6 -13,-15 0,0 -13,15 -13,6 -42,6"/>
  </defs>

  <text class="headline" x="905" y="240" font-size="78" textLength="415" lengthAdjust="spacingAndGlyphs">MES PLANS</text>

  <rect class="rule-bar" x="705" y="288" width="123" height="32"/>
  <text class="headline" x="908" y="329" font-size="68">DE</text>
  <rect class="rule-bar" x="988" y="288" width="124" height="32"/>

  <g class="pointers">
    <use href="#pointer-arrow" transform="translate(766 404) rotate(35)"/>
    <use href="#pointer-arrow" transform="translate(740 462) rotate(10)"/>
    <use href="#pointer-arrow" transform="translate(760 688) rotate(-45)"/>
    <use href="#pointer-arrow" transform="translate(1044 404) rotate(145)"/>
    <use href="#pointer-arrow" transform="translate(1070 462) rotate(170)"/>
    <use href="#pointer-arrow" transform="translate(1050 688) rotate(-135)"/>
  </g>

  <circle class="globe-area" cx="905" cy="510" r="155" role="img" aria-label="Globe terrestre dessiné à l'encre montrant les continents"/>

  <g class="ribbon">
    <polygon class="ribbon-part" points="735,535 648,545 672,575 650,610 740,600"/>
    <polygon class="ribbon-part" points="1075,535 1160,545 1138,575 1160,610 1070,600"/>
    <polygon class="ribbon-part" points="722,497 1088,497 1082,567 728,567"/>
    <text class="ribbon-word" x="905" y="547" font-size="44" textLength="320" lengthAdjust="spacingAndGlyphs">DOMINATION</text>
  </g>

  <text class="headline" x="910" y="782" font-size="76" textLength="405" lengthAdjust="spacingAndGlyphs">MONDIALE</text>
</svg>
</body>
</html>
```